Recruiting agency needs corporate presentation

We are a recruiting agency specialized in life sciences. We need a corporate presentation that will be sent to our clients and prospects in a PDF format.

Details of the presentation:
- a "brochure" type of presentation, VERTICAL, with 5 pages (please see "content" file attached) The presentation will be sent in a PDF format to our prospect clients by e-mail, so the choice of images and organization need to take that into account.
- In the attachment, you will find our logo "Harlow & Associates".
- the presentation needs to convey our industry (life sciences, healthcare) and a high level of professionalism/leadership We want a sophisticated and elegant brochure.
- page 2 of the brochure needs to contain all the logos attached, in a very elegant, clear and organized way.
- page 3 shows a map with cursors (please see content file). The following countries/continents on the map need to be highlighted: USA, Brazil, Europe, North Africa, South Africa, China. We need "cursors" like pins to show where on the map our offices are: Miami, Boston, Lausanne, Denmark, Paris, Copenhaguen.
- page 4 includes pie charts (please see "Statistics 2020" Excel file): please improve the pie charts aesthetics, it needs to look very modern.

Target Market(s)

Healthcare / Life Sciences.

Requirements
Must have
• Very modern and aesthetics. I included a presentation of companies that we like to give you an indication of the overall style we're looking for.

```html
<!DOCTYPE html>
<html lang="en">
<head>
<meta charset="utf-8">
<title>Harlow &amp; Associates – Corporate Brochure</title>
<link href="https://fonts.googleapis.com/css2?family=Montserrat:wght@500;600;700;800&family=Arimo:wght@400;700&display=swap" rel="stylesheet">
<style>
:root{
  --gold:#d6a92c;
  --gold-light:#e7c55d;
  --ink:#0f0f0f;
  --grey:#7c7c7c;
  --grey-mid:#9a9a9a;
  --grey-light:#c9c9c9;
  --cream:#ece4cc;
  --cream-light:#f4efe0;
  --text:#333;
  --paper:#fff;
  --client-blue:#2d3e73;
  --client-red:#c42a2a;
  --client-grey:#555;
  --client-green:#2f7a4a;
}
*{box-sizing:border-box;margin:0;padding:0}
html,body{width:1200px;height:1000px;overflow:hidden}
body{background:linear-gradient(#f7f7f7,#e6e6e6);font-family:"Arimo",Arial,sans-serif;color:var(--text);position:relative}
.page{position:absolute;width:399px;height:310px;background:var(--paper);box-shadow:0 3px 10px rgba(0,0,0,.18);overflow:hidden}
.page .band{position:absolute;left:0;right:0;bottom:0;height:10px;background:var(--gold)}
.heading{font-family:"Montserrat",Arial,sans-serif;font-weight:700;color:var(--ink);font-size:8.5px;letter-spacing:.2px}
.rule{position:absolute;width:30px;height:1.5px;background:var(--gold)}
.copy{font-size:5.4px;line-height:1.45;color:var(--text)}

/* cover */
.cover{left:209px;top:15px}
.cover .lines{position:absolute;inset:0;background:
  radial-gradient(ellipse 70% 45% at 85% 8%,rgba(214,169,44,.22),transparent 70%),
  radial-gradient(ellipse 70% 45% at 10% 92%,rgba(214,169,44,.2),transparent 70%)}
.cover .brand{position:absolute;left:0;right:0;top:120px;text-align:center}
.cover .brand-mark{display:block;width:46px;height:46px;border-radius:50%;background:#2a2a2a;margin:0 auto 10px}
.cover .brand-name{font-family:"Montserrat",Arial,sans-serif;font-weight:700;font-size:13px;letter-spacing:2.4px;color:var(--ink)}
.cover .brand-tag{font-family:"Montserrat",Arial,sans-serif;font-weight:700;font-size:5.6px;letter-spacing:1.6px;color:var(--ink);margin-top:2px}
.cover .site{position:absolute;left:0;right:0;top:288px;text-align:center;font-family:"Montserrat",Arial,sans-serif;font-weight:600;font-size:6px;color:var(--gold)}

/* offices */
.offices{left:629px;top:15px}
.offices .map{position:absolute;left:150px;top:10px;width:249px;height:225px;background:radial-gradient(ellipse at 50% 45%,#cfcfcf,#ececec 60%,#fafafa 80%)}
.offices .heading{position:absolute;left:17px;top:110px}
.offices .rule{left:17px;top:104px}
.offices .copy{position:absolute;left:17px;top:130px;width:128px}
.offices svg{position:absolute;inset:0}
.pin-label{position:absolute;background:var(--gold);color:#fff;font-family:"Montserrat",Arial,sans-serif;font-weight:600;font-size:3.8px;padding:1.2px 4px;border-radius:2px;letter-spacing:.3px}

/* about */
.about{left:209px;top:340px}
.about .photo{position:absolute;left:0;top:0;width:239px;height:300px;background:linear-gradient(120deg,#e9eef4 0%,#c8d6e6 40%,#f2f3f5 70%,#6f8fb8 100%)}
.about .rule{left:254px;top:108px}
.about .heading{position:absolute;left:254px;top:115px}
.about .copy{position:absolute;left:254px;top:134px;width:130px}
.about .copy p+p{margin-top:6px}

/* sectors */
.sectors{left:629px;top:340px}
.sectors .intro{position:absolute;left:0;top:22px;width:171px;height:65px;background:var(--ink);padding:12px 16px}
.sectors .intro h2{font-family:"Montserrat",Arial,sans-serif;font-weight:700;font-size:7.2px;color:var(--gold);margin-bottom:7px}
.sectors .intro p{font-size:5px;line-height:1.4;color:#fff}
.sectors .function-title{position:absolute;left:17px;top:102px}
.pie{position:absolute;left:38px;top:115px;width:110px;height:110px;border-radius:50%;
  background:conic-gradient(var(--grey) 0 5.8%,var(--grey-mid) 5.8% 10.5%,var(--gold-light) 10.5% 38%,var(--gold) 38% 67%,var(--cream) 67% 71.8%,var(--cream-light) 71.8% 81%,var(--ink) 81% 100%)}
.pie-val{position:absolute;transform:translate(-50%,-50%);font-family:"Montserrat",Arial,sans-serif;font-weight:700;font-size:4.6px;color:#fff}
.pie-val.dark{color:#555}
.legend{position:absolute;left:20px;top:244px;display:grid;grid-template-columns:88px 88px;row-gap:3.5px;font-size:5.2px;color:var(--text)}
.legend span{display:flex;align-items:flex-start;gap:5px;line-height:1.2}
.legend i{display:inline-block;width:4px;height:4px;border-radius:50%;margin-top:1px;flex:none}
.sectors .sector-title{position:absolute;left:186px;top:22px}
.donut{position:absolute;left:245px;top:47px;width:92px;height:92px;border-radius:50%;
  background:conic-gradient(var(--grey-light) 0 3%,var(--gold) 3% 34%,var(--gold-light) 34% 38%,var(--ink) 38% 61%,#3a3a3a 61% 75%,var(--grey) 75% 84%,var(--grey-mid) 84% 93%,#dcdcdc 93% 96%,var(--cream) 96% 100%)}
.donut::after{content:"";position:absolute;left:11px;top:11px;width:70px;height:70px;border-radius:50%;background:#fff}
.tag{position:absolute;background:var(--gold);color:#fff;font-family:"Montserrat",Arial,sans-serif;font-weight:600;font-size:3.9px;padding:1.3px 4px;border-radius:1.5px;white-space:nowrap}
.sectors .seniority-title{position:absolute;left:186px;top:182px}
.seniority{position:absolute;left:188px;top:202px}
.seniority .row{display:flex;align-items:center;height:20px}
.people{display:flex;gap:2.5px;width:68px}
.person{position:relative;width:9.5px;height:11px}
.person::before{content:"";position:absolute;left:2.5px;top:0;width:4.5px;height:4.5px;border-radius:50%;background:currentColor}
.person::after{content:"";position:absolute;left:0;top:5px;width:9.5px;height:6px;border-radius:4px 4px 0 0;background:currentColor}
.person.on{color:var(--gold)}
.person.off{color:var(--grey)}
.pill{display:flex;align-items:center;gap:6px;width:117px;height:8px;border:.8px solid var(--gold);border-radius:5px;font-family:"Montserrat",Arial,sans-serif;font-size:4.4px;font-weight:600;color:var(--ink);overflow:hidden}
.pill b{background:var(--gold);color:#fff;height:100%;padding:0 5px;display:flex;align-items:center;border-radius:5px}
.sectors .footnote{position:absolute;right:12px;top:287px;font-size:4.4px;font-style:italic;color:#555}

/* clients */
.clients{left:209px;top:662px}
.clients .header{position:absolute;left:0;top:0;width:100%;height:48px;background:#121212;text-align:center;padding-top:13px}
.clients .header h2{font-family:"Montserrat",Arial,sans-serif;font-weight:700;font-size:8.5px;color:var(--gold)}
.clients .header p{font-size:5.2px;color:#fff;margin-top:4px}
.client-grid{position:absolute;left:12px;right:12px;top:58px;display:grid;grid-template-rows:repeat(7,34px)}
.client-row{display:flex;justify-content:space-between;align-items:center}
.client{display:flex;align-items:center;gap:2px;font-family:"Montserrat",Arial,sans-serif;font-weight:700;font-size:5px;color:var(--client-blue);white-space:nowrap}
.client.red{color:var(--client-red)}
.client.grey{color:var(--client-grey)}
.client.green{color:var(--client-green)}
.client i{display:inline-block;width:5px;height:5px;border-radius:50%;background:currentColor}

/* thanks */
.thanks{left:629px;top:662px;background:#060606}
.thanks .waves{position:absolute;inset:0;background:
  radial-gradient(ellipse 60% 30% at 90% 10%,rgba(120,120,120,.35),transparent 70%),
  radial-gradient(ellipse 70% 30% at 30% 95%,rgba(150,150,150,.35),transparent 70%)}
.thanks .message{position:absolute;left:0;right:0;top:120px;text-align:center;font-family:"Montserrat",Arial,sans-serif;font-weight:700;font-size:8px;line-height:1.8;color:var(--gold)}
.thanks .contacts{position:absolute;left:0;right:0;top:158px;display:flex;justify-content:center;gap:30px;font-size:5.2px;color:#fff}
.thanks .contacts span{display:flex;align-items:center;gap:4px}
.thanks .contacts i{display:inline-block;width:5px;height:3.5px;background:var(--gold);border-radius:.5px}
.thanks .contacts i.globe{width:4.5px;height:4.5px;border-radius:50%}
</style>
</head>
<body>

<!-- Cover -->
<section class="page cover">
  <div class="lines" role="img" aria-label="Fine flowing gold line pattern"></div>
  <div class="brand">
    <span class="brand-mark" role="img" aria-label="Brand emblem"></span>
    <div class="brand-name">HARLOW &amp; ASSOCIATES</div>
    <div class="brand-tag">GLOBAL LIFE SCIENCES RECRUITING</div>
  </div>
  <div class="site">www.harlowassociates.com</div>
</section>

<!-- Offices -->
<section class="page offices">
  <div class="map" role="img" aria-label="Dotted world map highlighting office regions"></div>
  <svg viewBox="0 0 399 310" width="399" height="310" aria-hidden="true">
    <g stroke="#d6a92c" stroke-width=".6" fill="none">
      <polyline points="190,50 206,50 206,150"/>
      <polyline points="204,68 216,68 216,130"/>
      <polyline points="290,68 271,68 271,110"/>
      <polyline points="300,84 279,84 279,114"/>
      <polyline points="256,222 268,222 268,140"/>
      <polyline points="275,241 296,241 296,145"/>
    </g>
    <g fill="#d6a92c">
      <path d="M206 158c-3-4-5-6-5-9a5 5 0 0 1 10 0c0 3-2 5-5 9z"/>
      <path d="M216 138c-3-4-5-6-5-9a5 5 0 0 1 10 0c0 3-2 5-5 9z"/>
      <path d="M271 118c-3-4-5-6-5-9a5 5 0 0 1 10 0c0 3-2 5-5 9z"/>
      <path d="M279 122c-3-4-5-6-5-9a5 5 0 0 1 10 0c0 3-2 5-5 9z"/>
      <path d="M268 142c-3-4-5-6-5-9a5 5 0 0 1 10 0c0 3-2 5-5 9z"/>
      <path d="M296 147c-3-4-5-6-5-9a5 5 0 0 1 10 0c0 3-2 5-5 9z"/>
    </g>
    <g fill="#fff">
      <circle cx="206" cy="149" r="2"/><circle cx="216" cy="129" r="2"/><circle cx="271" cy="109" r="2"/>
      <circle cx="279" cy="113" r="2"/><circle cx="268" cy="133" r="2"/><circle cx="296" cy="138" r="2"/>
    </g>
  </svg>
  <span class="pin-label" style="left:174px;top:45px">MIAMI</span>
  <span class="pin-label" style="left:187px;top:63px">BOSTON</span>
  <span class="pin-label" style="left:276px;top:63px">DENMARK</span>
  <span class="pin-label" style="left:284px;top:79px">COPENHAGEN</span>
  <span class="pin-label" style="left:241px;top:217px">PARIS</span>
  <span class="pin-label" style="left:257px;top:236px">LAUSANNE</span>
  <span class="rule"></span>
  <h2 class="heading">OUR OFFICES</h2>
  <div class="copy">
    <p>Harlow &amp; Associates' global success is driven by our multi-cultural team's ability to orchestrate an operational, innovative and direct approach to recruiting.</p>
    <p style="margin-top:6px">Thanks to our global presence and proprietary offices in Europe and in the U.S., we have placed thousands of professionals in companies over <b>30 countries and 5 continents.</b></p>
  </div>
  <div class="band"></div>
</section>

<!-- About -->
<section class="page about">
  <div class="photo" role="img" aria-label="Two scientists in lab coats and safety glasses reviewing results in a laboratory"></div>
  <span class="rule"></span>
  <h2 class="heading">ABOUT US</h2>
  <div class="copy">
    <p>We are an international recruiting boutique agency specialized in Life Sciences. In the last 3 decades, we have appointed thousands of professionals globally.</p>
    <p>Our firm is known for being highly committed and able to deliver great results within budget and timing constraints. Equality and parity are at the core of our activity.</p>
  </div>
  <div class="band"></div>
</section>

<!-- Sectors & functions -->
<section class="page sectors">
  <div class="intro">
    <h2>SECTORS &amp; FUNCTIONS</h2>
    <p>We cover all sectors and all functions within Life Sciences. Each client is unique. Our solutions are tailor-made to your organization.</p>
  </div>
  <h2 class="heading function-title">FUNCTION</h2>
  <div class="pie" role="img" aria-label="Placements by function pie chart"></div>
  <span class="pie-val" style="left:99px;top:136px">5.8%</span>
  <span class="pie-val" style="left:110px;top:139px">4.7%</span>
  <span class="pie-val" style="left:128px;top:168px">27.5%</span>
  <span class="pie-val" style="left:88px;top:205px">29%</span>
  <span class="pie-val dark" style="left:63px;top:189px">4.8%</span>
  <span class="pie-val dark" style="left:60px;top:172px">9.2%</span>
  <span class="pie-val" style="left:75px;top:141px">19.1%</span>
  <div class="legend">
    <span><i style="background:var(--cream-light);border:.4px solid #ccc"></i>HR</span>
    <span><i style="background:var(--ink)"></i>R&amp;D</span>
    <span><i style="background:var(--cream)"></i>INDUSTRIAL</span>
    <span><i style="background:var(--grey)"></i>QUALITY</span>
    <span><i style="background:var(--gold-light)"></i>SALES / BUSINESS DEV</span>
    <span><i style="background:var(--grey-mid)"></i>FINANCE / LEGAL</span>
    <span><i style="background:var(--gold)"></i>MEDICAL / REG /<br>MARKET ACCESS</span>
  </div>

  <h2 class="heading sector-title">SECTORS</h2>
  <div class="donut" role="img" aria-label="Placements by sector donut chart"></div>
  <span class="pie-val dark" style="left:287px;top:57px">3%</span>
  <span class="pie-val" style="left:327px;top:79px">31%</span>
  <span class="pie-val" style="left:327px;top:119px">4%</span>
  <span class="pie-val" style="left:285px;top:133px">23%</span>
  <span class="pie-val" style="left:251px;top:103px">14%</span>
  <span class="pie-val" style="left:253px;top:84px">9%</span>
  <span class="pie-val" style="left:263px;top:67px">9%</span>
  <span class="pie-val dark" style="left:275px;top:59px">3%</span>
  <svg style="position:absolute;left:0;top:0" width="399" height="310" aria-hidden="true">
    <g stroke="#d6a92c" stroke-width=".5" fill="none">
      <polyline points="226,46 272,46 272,58"/>
      <polyline points="218,68 258,68 262,72"/>
      <polyline points="215,111 247,111"/>
      <polyline points="210,154 240,154 250,120"/>
      <polyline points="330,46 300,46 292,55"/>
      <polyline points="330,79 334,79"/>
      <polyline points="330,124 326,124 324,122"/>
      <polyline points="330,155 300,155 290,138"/>
    </g>
  </svg>
  <span class="tag" style="left:186px;top:42px">ANIMAL HEALTH</span>
  <span class="tag" style="left:186px;top:64px">DIGITAL HEALTH</span>
  <span class="tag" style="left:186px;top:107px">NUTRITION</span>
  <span class="tag" style="left:186px;top:150px">PHARMA</span>
  <span class="tag" style="left:330px;top:42px">HOSPITAL &amp; CLINICS</span>
  <span class="tag" style="left:356px;top:75px">BIOTECH</span>
  <span class="tag" style="left:356px;top:120px">MEDTECH</span>
  <span class="tag" style="left:336px;top:151px">MEDICAL DEVICE</span>

  <h2 class="heading seniority-title">SENIORITY</h2>
  <div class="seniority">
    <div class="row">
      <div class="people"><span class="person on"></span><span class="person off"></span><span class="person off"></span><span class="person off"></span><span class="person off"></span></div>
      <div class="pill"><b>9.1%</b>BOARD MEMBERS</div>
    </div>
    <div class="row">
      <div class="people"><span class="person on"></span><span class="person on"></span><span class="person off"></span><span class="person off"></span><span class="person off"></span></div>
      <div class="pill"><b>33.4%</b>TOP MANAGEMENT</div>
    </div>
    <div class="row">
      <div class="people"><span class="person on"></span><span class="person on"></span><span class="person off"></span><span class="person off"></span><span class="person off"></span></div>
      <div class="pill"><b>23.6%</b>EXPERT MANAGEMENT</div>
    </div>
    <div class="row">
      <div class="people"><span class="person on"></span><span class="person on"></span><span class="person on"></span><span class="person off"></span><span class="person off"></span></div>
      <div class="pill"><b>33.9%</b>MIDDLE MANAGEMENT</div>
    </div>
  </div>
  <p class="footnote">*base on the last 5 years results.</p>
  <div class="band"></div>
</section>

<!-- Clients -->
<section class="page clients">
  <div class="header">
    <h2>OUR CLIENTS</h2>
    <p>Our clients range from innovative start-ups to leading global corporations</p>
  </div>
  <div class="client-grid">
    <div class="client-row">
      <span class="client"><i></i>Kestrel</span><span class="client red">Lumora</span><span class="client">Veyra Gas</span><span class="client"><i></i>Opalis</span><span class="client">Tridan</span><span class="client">Solvane</span><span class="client grey">Merrow</span><span class="client green">Quellis</span><span class="client red">Halvorn</span><span class="client grey">Brisca</span><span class="client red">Zento</span>
    </div>
    <div class="client-row">
      <span class="client">Corlan</span><span class="client"><i></i>NX</span><span class="client">Elmfield Health</span><span class="client red">Arkwell</span><span class="client grey">Tessaro</span><span class="client red">Ondo</span><span class="client grey">Pravix</span><span class="client">Marlo Pharma</span><span class="client">Sydra</span><span class="client">Culvert</span><span class="client green">Pelora</span>
    </div>
    <div class="client-row">
      <span class="client">Wrenfield</span><span class="client">Fennick</span><span class="client green">Orisel</span><span class="client">Talvo</span><span class="client green">Cirana</span><span class="client green">Mireau</span><span class="client">Dovecot</span><span class="client"><i></i>Heron Lab</span><span class="client">Ashby Vale</span><span class="client">Larkspur</span><span class="client">Embry</span>
    </div>
    <div class="client-row">
      <span class="client">Quarry Lab</span><span class="client">Belvis</span><span class="client grey">RTQ</span><span class="client red">Nimbra</span><span class="client red">Caldor</span><span class="client red">Wexley</span><span class="client">Saffra</span><span class="client">Torvik</span><span class="client"><i></i>Linden Care</span><span class="client red">Ivory Medica</span><span class="client">Plexa</span>
    </div>
    <div class="client-row">
      <span class="client green">Tamsin</span><span class="client grey">Orlo</span><span class="client">Ferrow</span><span class="client grey">Northway Bio</span><span class="client red"><i></i>Arlen</span><span class="client">Calloway</span><span class="client">Institut Solenne</span><span class="client">Dravo</span><span class="client grey">Penwick</span><span class="client">Strand</span><span class="client green">Mossley</span>
    </div>
    <div class="client-row">
      <span class="client grey">Brindle</span><span class="client">Velmont</span><span class="client">Ciro</span><span class="client grey">Halden</span><span class="client"><i></i>Ovaro</span><span class="client">Tolland</span><span class="client">Greyburn</span><span class="client grey">Nestwell</span><span class="client red">Ardmore</span><span class="client grey">Lyse</span><span class="client red">Caravel Onco</span>
    </div>
    <div class="client-row">
      <span class="client">Fernbrook</span><span class="client grey">Sextan</span><span class="client red">Quillon</span><span class="client red">Rosk</span><span class="client">Alder</span><span class="client red">Miro</span><span class="client grey">Elowen</span><span class="client"><i></i>Bexley</span><span class="client red">Corrin</span><span class="client red">Vantara</span>
    </div>
  </div>
  <div class="band"></div>
</section>

<!-- Thank you -->
<section class="page thanks">
  <div class="waves" role="img" aria-label="Flowing silver line pattern"></div>
  <p class="message">Thank you for your consideration.<br>We are looking forward to speaking with you.</p>
  <div class="contacts">
    <span><i></i>recruitment@harlowassociates.com</span>
    <span><i class="globe"></i>www.harlowassociates.com</span>
  </div>
  <div class="band"></div>
</section>

</body>
</html>
```